SKYWARD LENSWORKS New Wordpress Design Project

Skyward Lensworks is a photo-sharing site for aviation photographers and enthusiasts.

Please redesign the home page (http://www.skywardlensworks.example/) and photo feature page (http://www.skywardlensworks.example/2014/10/borealis-freight-23/).

We like and would like to keep the logo we have, but are open to changing colors on the logo to suit a new color scheme if necessary.
Updates

Hi All, Thank you for taking part in this design competition. Could you please show us your first round design concepts within 24hrs as we hope to show our client them and start providing feedback? Much appreciated, Nils Brandvik PebbleQuay Design

Hi All, A few tips: Could you try keep the search bar above the fold Include a section for showing new blog posts Try to integrate an ads a little better also above and below the fold Appreciated, Nils Brandvik

Target Market(s)

Aviation photographers and enthusiasts of all age groups globally.

Industry/Entity Type

Aviation

Requirements
Must have
• • Clean and consistent layout
• A good way to incorporate advertisements on the home page and photo feature page
• Clear and simple menu navigation
• On home page – call to action to register
• On home page - call to action to upload photos
• On home page – social buttons call to action to follow, circle, like, etc
• On photo feature page – call to action to tweet, +1, Like, etc a photo
Nice to have
• Sites we like

www.frametide.example
http://www.layoutharbor.example/demo/83912.html
Should not have
• • Unnecessary animations
• No Adobe Flash
• Overly crowded / busy design

```html
<!DOCTYPE html>
<html lang="en">
<head>
<meta charset="utf-8">
<title>Skyward Lensworks – Home</title>
<link rel="stylesheet" href="https://fonts.googleapis.com/css2?family=Ubuntu:wght@400;500;700&display=swap">
<style>
  :root {
    --orange: #f0900f;
    --orange-light: #f7a93a;
    --orange-dark: #d97c06;
    --ink: #111111;
    --brown: #3e2410;
    --brown-text: #6b3a10;
    --grey-text: #9a9a9a;
    --hero-deep: #0d2446;
    --hero-mid: #1f4a7c;
    --white: #ffffff;
    --footer-bar: #8c8c8c;
    --quote-text: #cdbb9c;
  }
  * { box-sizing: border-box; margin: 0; padding: 0; }
  html, body { width: 1200px; height: 2442px; overflow: hidden; }
  body {
    position: relative;
    background: var(--white);
    font-family: "Ubuntu", sans-serif;
    color: var(--ink);
  }
  .abs { position: absolute; }

  /* Header */
  .brand {
    left: 130px; top: 34px; height: 44px;
    display: flex; align-items: center; gap: 10px;
    font-size: 26px; font-weight: 700; color: var(--ink); letter-spacing: -0.3px;
  }
  .brand-dot { width: 16px; height: 16px; border-radius: 50%; background: var(--orange); }
  .main-nav {
    left: 396px; top: 29px; width: 703px; height: 49px;
    background: var(--orange); display: flex; align-items: center;
    font-size: 17px; font-weight: 500;
  }
  .main-nav a { color: var(--ink); text-decoration: none; padding: 0 22px; height: 100%; display: flex; align-items: center; }
  .main-nav a.is-active { background: var(--ink); color: var(--white); width: 92px; justify-content: center; padding: 0; }
  .nav-search {
    margin-left: auto; margin-right: 28px; width: 139px; height: 30px;
    background: #fff8ee; border: 1px solid #f7d6a6; color: #b9b9b9;
    font-size: 15px; padding: 5px 12px;
  }

  /* Hero */
  .hero {
    left: 0; top: 94px; width: 1200px; height: 489px;
    background: radial-gradient(ellipse at 65% 45%, var(--hero-mid), var(--hero-deep) 75%);
  }
  .hero-panel {
    left: 208px; top: 199px; width: 782px; height: 293px;
    background: rgba(12, 22, 38, 0.72); text-align: center; color: var(--white);
  }
  .hero-title { margin-top: 26px; font-size: 30px; font-weight: 500; }
  .hero-title span { color: var(--orange); }
  .hero-text { width: 640px; margin: 14px auto 0; font-size: 17.5px; line-height: 25px; }
  .hero-actions { position: absolute; left: 82px; top: 200px; display: flex; gap: 82px; }
  .hero-btn {
    width: 139px; height: 49px; background: linear-gradient(var(--orange-light), var(--orange-dark));
    color: var(--white); font-size: 24px; font-weight: 500; display: flex; align-items: center; justify-content: center;
    box-shadow: 0 2px 4px rgba(0,0,0,.4);
  }
  .slider-dots { left: 148px; top: 531px; display: flex; gap: 14px; }
  .slider-dots i { width: 17px; height: 17px; border-radius: 50%; background: var(--white); display: block; }
  .slider-dots i.is-current { background: var(--orange); border: 2px solid #ffd27a; }

  /* Section headings */
  .section-title { font-size: 38px; font-weight: 500; letter-spacing: 0.5px; }
  .section-title span { color: var(--orange); }
  .dotted-rule {
    height: 18px;
    background-image: radial-gradient(circle, #ddd 1.3px, transparent 1.6px);
    background-size: 5px 5px;
  }

  /* Gallery */
  .gallery-title { left: 137px; top: 622px; }
  .gallery-rule { left: 711px; top: 640px; width: 359px; }
  .gallery-intro { left: 137px; top: 692px; width: 620px; font-size: 17px; line-height: 25px; color: var(--grey-text); }
  .photo-card { width: 264px; }
  .photo-frame {
    width: 264px; height: 265px; border: 2px solid var(--orange-light);
    border-radius: 2px 2px 14px 10px; box-shadow: 2px 3px 6px rgba(0,0,0,.18);
  }
  .photo-tape {
    position: absolute; left: -34px; top: -12px; width: 110px; height: 36px;
    background: linear-gradient(#eeeeee, #cfcfcf); transform: rotate(-52deg);
    opacity: .92; box-shadow: 0 1px 2px rgba(0,0,0,.2);
  }
  .photo-caption { margin-top: 20px; text-align: center; font-size: 17px; font-weight: 500; color: var(--brown-text); }
  .sky-blue { background: linear-gradient(160deg, #2f6fc0, #8fc1ea); }
  .sky-cloud { background: linear-gradient(170deg, #3d7fcf, #cfe3f3 70%, #f2f6f8); }
  .sky-sunset { background: linear-gradient(#f5c45a, #b68656 55%, #58493c); }
  .runway-dusk { background: linear-gradient(#f3d18c, #c8a46e 55%, #6d5a44); }
  .ocean-deep { background: linear-gradient(150deg, #15325a, #2a5685); }
  .sky-pale { background: linear-gradient(#6e9cc0, #d6e6ef); }

  .more-btn {
    left: 270px; top: 1516px; width: 661px; height: 63px;
    background: linear-gradient(var(--orange-light), var(--orange-dark));
    border: 2px solid #fbc36a; box-shadow: 0 3px 5px rgba(0,0,0,.3);
    display: flex; align-items: center; justify-content: center;
    font-size: 35px; font-weight: 500; color: var(--ink);
  }

  /* Lower backdrop */
  .runway-scene {
    left: 0; top: 1500px; width: 1200px; height: 877px;
    background: linear-gradient(#ffffff 0%, #f8f4ee 35%, #ece6dc 62%, #b9b8a6 78%, #9c9b92 100%);
  }

  /* Testimonial */
  .voices-title { left: 133px; top: 1662px; }
  .voices-rule { left: 594px; top: 1680px; width: 476px; }
  .avatar {
    left: 226px; top: 1747px; width: 95px; height: 95px; border-radius: 50%;
    border: 3px solid var(--orange); background: linear-gradient(#e9d6b0, #c9a377);
  }
  .voice-name { left: 342px; top: 1756px; font-size: 21px; }
  .voice-role { left: 342px; top: 1790px; font-size: 17px; color: var(--orange); }
  .quote-box {
    left: 130px; top: 1849px; width: 940px; height: 183px;
    background: var(--brown); border-radius: 4px; box-shadow: 0 3px 6px rgba(0,0,0,.3);
  }
  .quote-tail { left: 200px; top: 1826px; }
  .quote-text {
    position: absolute; left: 60px; top: 46px; width: 820px; text-align: center;
    font-size: 17px; line-height: 25px; color: var(--quote-text); font-weight: 500;
  }
  .quote-mark { position: absolute; font-size: 110px; color: #7a6a5a; font-family: Georgia, serif; line-height: 1; }

  /* Footer */
  .footer-head { font-size: 21px; font-weight: 500; color: #2a2a2a; letter-spacing: .5px; }
  .footer-text { font-size: 17px; line-height: 25px; color: #2a2a2a; }
  .newsletter { left: 192px; top: 2135px; width: 290px; }
  .newsletter .footer-text { width: 280px; }
  .email-field {
    margin-top: 28px; width: 280px; height: 39px; background: #9a9a94;
    border: 2px solid #c8c8c0; color: var(--white); font-size: 16px; padding: 8px 10px;
  }
  .submit-btn {
    margin-top: 19px; margin-left: 3px; width: 83px; height: 33px;
    background: linear-gradient(var(--orange-light), var(--orange-dark));
    color: var(--ink); font-size: 16px; display: flex; align-items: center; justify-content: center;
    box-shadow: 0 2px 3px rgba(0,0,0,.3);
  }
  .divider { width: 1px; height: 227px; top: 2133px; background: rgba(60,60,60,.45); }
  .quick-links { left: 558px; top: 2135px; }
  .quick-links ul { list-style: none; margin-top: 8px; margin-left: 5px; }
  .quick-links li { font-size: 17px; height: 37.5px; color: #2a2a2a; }
  .follow { left: 803px; top: 2135px; }
  .social-grid { margin-top: 14px; display: grid; grid-template-columns: repeat(4, 40px); column-gap: 14px; row-gap: 22px; }
  .social-grid i { display: block; width: 40px; height: 40px; border-radius: 6px; }
  .s1 { background: #3aa9e0; } .s2 { background: #d8342c; } .s3 { background: #3b5a99; } .s4 { background: #1f7bb4; }
  .s5 { background: #c8202c; } .s6 { background: #d9462f; } .s7 { background: #ee7a18; } .s8 { background: #f08a1e; }
  .copyright {
    left: 0; top: 2377px; width: 1200px; height: 65px; background: var(--footer-bar);
    color: var(--white); font-size: 16px; display: flex; align-items: center; justify-content: center;
  }
</style>
</head>
<body>

<header>
  <div class="abs brand"><i class="brand-dot"></i>Skyward Lensworks</div>
  <nav class="abs main-nav">
    <a class="is-active">Home</a>
    <a>Gallery</a>
    <a>Submit a photo</a>
    <a>Airport search</a>
    <div class="nav-search">Search</div>
  </nav>
</header>

<section>
  <div class="abs hero" role="img" aria-label="Business jet flying low over a deep blue sea"></div>
  <div class="abs hero-panel">
    <h1 class="hero-title">Get Connect With <span>Skyward Lensworks</span></h1>
    <p class="hero-text">Lorem Ipsum is simply dummy text of the printing and typesetting industry. Lorem Ipsum has been the industry's standard dummy text ever since the 1500s, when an unknown printer took a galley of type and scrambled it to make a type specimen book.</p>
    <div class="hero-actions">
      <div class="hero-btn">LOGIN</div>
      <div class="hero-btn">REGISTER</div>
      <div class="hero-btn">UPLOAD</div>
    </div>
  </div>
  <div class="abs slider-dots"><i class="is-current"></i><i></i><i></i><i></i></div>
</section>

<section>
  <h2 class="abs section-title gallery-title"><span>Skyward</span> Lensworks Gallery</h2>
  <div class="abs dotted-rule gallery-rule"></div>
  <p class="abs gallery-intro">Lorem Ipsum is simply dummy text of the printing and typesetting industry. Lorem Ipsum has been the industry's standard dummy text ever</p>

  <figure class="abs photo-card" style="left:163px;top:790px">
    <div class="photo-frame sky-blue" role="img" aria-label="Airliner climbing into a bright blue sky"></div>
    <span class="photo-tape"></span>
    <figcaption class="photo-caption">ipsum quia dolor sit</figcaption>
  </figure>
  <figure class="abs photo-card" style="left:483px;top:790px">
    <div class="photo-frame sky-cloud" role="img" aria-label="Red and white airliner among white clouds"></div>
    <span class="photo-tape"></span>
    <figcaption class="photo-caption">ipsum quia dolor sit</figcaption>
  </figure>
  <figure class="abs photo-card" style="left:803px;top:790px">
    <div class="photo-frame sky-sunset" role="img" aria-label="Airliner above clouds at sunset"></div>
    <span class="photo-tape"></span>
    <figcaption class="photo-caption">ipsum quia dolor sit</figcaption>
  </figure>
  <figure class="abs photo-card" style="left:163px;top:1166px">
    <div class="photo-frame runway-dusk" role="img" aria-label="Airliner landing over a runway at dusk"></div>
    <span class="photo-tape"></span>
    <figcaption class="photo-caption">ipsum quia dolor sit</figcaption>
  </figure>
  <figure class="abs photo-card" style="left:483px;top:1166px">
    <div class="photo-frame ocean-deep" role="img" aria-label="Business jet over dark blue ocean"></div>
    <span class="photo-tape"></span>
    <figcaption class="photo-caption">ipsum quia dolor sit</figcaption>
  </figure>
  <figure class="abs photo-card" style="left:803px;top:1166px">
    <div class="photo-frame sky-pale" role="img" aria-label="Airliner seen head-on in a pale cloudy sky"></div>
    <span class="photo-tape"></span>
    <figcaption class="photo-caption">ipsum quia dolor sit</figcaption>
  </figure>
</section>

<div class="abs runway-scene" role="img" aria-label="Hazy sky fading down to a long runway stretching to the horizon"></div>
<div class="abs more-btn">View More Photo Gallery</div>

<section>
  <h2 class="abs section-title voices-title">Our <span>Photographers</span> Says</h2>
  <div class="abs dotted-rule voices-rule"></div>
  <div class="abs avatar" role="img" aria-label="Portrait photo of the photographer"></div>
  <div class="abs voice-name">porro quisquam est</div>
  <div class="abs voice-role">dolorem ipsum</div>
  <svg class="abs quote-tail" width="30" height="26" viewBox="0 0 30 26" aria-hidden="true">
    <polygon points="24,0 30,26 0,26" fill="var(--brown)"/>
  </svg>
  <blockquote class="abs quote-box">
    <span class="quote-mark" style="left:12px;top:6px">“</span>
    <p class="quote-text">Lorem Ipsum is simply dummy text of the printing and typesetting industry. Lorem Ipsum has been the industry's standard dummy text ever since the 1500s, when an unknown printer took a galley of type and scrambled it to make a type specimen book. It has survived not only five cen-</p>
    <span class="quote-mark" style="right:12px;top:70px">”</span>
  </blockquote>
</section>

<footer>
  <div class="abs newsletter">
    <h3 class="footer-head">News Letter</h3>
    <p class="footer-text" style="margin-top:6px">when an unknown printer took a galley of type and scrambled it</p>
    <div class="email-field">Your E-mail</div>
    <div class="submit-btn">Submit</div>
  </div>
  <div class="abs divider" style="left:518px"></div>
  <div class="abs quick-links">
    <h3 class="footer-head">Quick Links</h3>
    <ul>
      <li>Home</li>
      <li>Gallery</li>
      <li>Submit a photo</li>
      <li>Airport search</li>
      <li>contact Us</li>
    </ul>
  </div>
  <div class="abs divider" style="left:749px"></div>
  <div class="abs follow">
    <h3 class="footer-head">Follow Us On</h3>
    <div class="social-grid" aria-label="Social network links">
      <i class="s1"></i><i class="s2"></i><i class="s3"></i><i class="s4"></i>
      <i class="s5"></i><i class="s6"></i><i class="s7"></i><i class="s8"></i>
    </div>
  </div>
  <div class="abs copyright">All Rights Reserved@ 2014 hello@skywardlensworks.example</div>
</footer>

</body>
</html>
```